Plumbing company needs Business Card Design

Hi I need business card design based on logo which I uploaded. Its plumbing and heating company called Kranex Usługi Hydrauliczno-Gazowe. I want to see on my card motto of my company which is "...od wymiany uszczelki po wymiane łazienki.", my phone number, name, and website: 617248390, Marek Kowalczyk, info@kranex.org, www.kranex.org
I want to see logos of companys which I'm approved installer (Termolux) (La Valmont) (Corvo) (Pluma).
I want new creative look of business card. I like rounded corners.
Any questions please send message.
Thanks for intrest.
Business
Contact Information for Business Card
Marek Kowalczyk
617 248 390
info@kranex.org
www.kranex.org
...od wymiany uszczelki po wymiane łazienki.

```html
<!DOCTYPE html>
<html lang="pl">
<head>
<meta charset="utf-8">
<title>Kranex – wizytówka</title>
<link rel="stylesheet" href="https://fonts.googleapis.com/css2?family=Quicksand:wght@500;700&display=swap">
<style>
  :root{
    --bg:#e4e3e0;
    --yellow:#f2c51c;
    --yellow-deep:#d9ab10;
    --ink:#1e1e1e;
    --charcoal:#2b2b2b;
    --charcoal-light:#3a3a3a;
    --panel:#323232;
    --text-light:#f1f1f1;
    --text-muted:#cfcfcf;
  }
  *{box-sizing:border-box;margin:0;padding:0}
  html,body{width:1200px;height:1000px;overflow:hidden}
  body{background:var(--bg);font-family:"Quicksand",sans-serif;position:relative}

  .card{position:absolute;left:180px;width:840px;height:460px;border-radius:22px;overflow:hidden;box-shadow:0 10px 26px rgba(0,0,0,.22)}
  .card--front{top:26px;background:var(--ink)}
  .card--back{top:514px;background:linear-gradient(160deg,var(--charcoal-light),var(--charcoal) 55%,#232323)}
  .front-frame,.back-panels{position:absolute;inset:0;width:100%;height:100%}

  .brand{position:absolute;display:flex;align-items:center;gap:22px}
  .brand__mark{background:var(--ink);border-radius:14px;flex:none}
  .brand__words{display:flex;flex-direction:column;font-weight:700;line-height:1}
  .brand__name{font-size:84px;letter-spacing:-1px}
  .brand__tagline{font-size:24px}
  .card--front .brand{left:210px;top:150px;color:var(--ink)}
  .card--front .brand__mark{width:120px;height:120px}

  .hazard-band{position:absolute;left:0;right:0;height:34px;
    background:linear-gradient(90deg,var(--yellow-deep),var(--yellow) 50%,var(--yellow-deep))}
  .hazard-band--top{top:0}
  .hazard-band--bottom{bottom:0}

  .card--back .brand{right:70px;top:74px;gap:14px;color:var(--yellow)}
  .card--back .brand__mark{width:66px;height:66px;background:var(--yellow);border-radius:10px}
  .card--back .brand__name{font-size:46px}
  .card--back .brand__tagline{font-size:13px}

  .holder{position:absolute;left:70px;top:252px;color:var(--text-light);font-size:28px;font-weight:700;line-height:1.2}
  .motto{position:absolute;left:330px;top:200px;color:var(--text-muted);font-size:15px;font-weight:500;line-height:1.2}
  .contacts{position:absolute;left:70px;right:70px;bottom:72px;display:flex;justify-content:space-between;list-style:none}
  .contacts li{display:flex;align-items:center;gap:12px;color:var(--text-light);font-size:20px;font-weight:500;white-space:nowrap}
  .icon{width:28px;height:28px;border-radius:50%;background:var(--yellow);display:flex;align-items:center;justify-content:center;flex:none}
</style>
</head>
<body>

<section class="card card--front" aria-label="Awers wizytówki">
  <svg class="front-frame" viewBox="0 0 840 460" aria-hidden="true">
    <polygon points="110,0 730,0 770,40 770,420 730,460 110,460 70,420 70,40" fill="var(--yellow)"/>
    <polyline points="40,70 90,70 120,40 720,40 750,70 800,70" fill="none" stroke="var(--ink)" stroke-width="2"/>
    <polyline points="40,390 90,390 120,420 720,420 750,390 800,390" fill="none" stroke="var(--ink)" stroke-width="2"/>
  </svg>
  <div class="brand">
    <div class="brand__mark"></div>
    <div class="brand__words">
      <span class="brand__name">Kranex</span>
      <span class="brand__tagline">Usługi Hydrauliczno-Gazowe</span>
    </div>
  </div>
</section>

<section class="card card--back" aria-label="Rewers wizytówki">
  <svg class="back-panels" viewBox="0 0 840 460" aria-hidden="true">
    <polygon points="0,34 840,34 840,130 760,170 80,170 0,130" fill="var(--panel)" opacity=".55"/>
    <polygon points="0,426 840,426 840,330 760,300 80,300 0,330" fill="var(--panel)" opacity=".45"/>
  </svg>

  <div class="hazard-band hazard-band--top" role="img" aria-label="Pas ostrzegawczy w żółto-czarne ukośne pasy"></div>
  <div class="hazard-band hazard-band--bottom" role="img" aria-label="Pas ostrzegawczy w żółto-czarne ukośne pasy"></div>

  <div class="brand">
    <div class="brand__mark"></div>
    <div class="brand__words">
      <span class="brand__name">Kranex</span>
      <span class="brand__tagline">Usługi Hydrauliczno-Gazowe</span>
    </div>
  </div>

  <p class="motto">od wymiany uszczelki po wymianę łazienki.</p>
  <p class="holder">Marek Kowalczyk</p>

  <ul class="contacts">
    <li>
      <span class="icon"><svg width="14" height="14" viewBox="0 0 24 24" aria-hidden="true"><path fill="#1e1e1e" d="M6.6 10.8a15 15 0 0 0 6.6 6.6l2.2-2.2c.3-.3.7-.4 1-.2 1.1.4 2.3.6 3.6.6.6 0 1 .4 1 1V20c0 .6-.4 1-1 1A17 17 0 0 1 3 4c0-.6.4-1 1-1h3.5c.6 0 1 .4 1 1 0 1.3.2 2.5.6 3.6.1.3 0 .7-.2 1z"/></svg></span>
      617 248 390
    </li>
    <li>
      <span class="icon"><svg width="14" height="14" viewBox="0 0 24 24" aria-hidden="true"><rect x="3" y="5" width="18" height="14" rx="1" fill="none" stroke="#1e1e1e" stroke-width="2"/><path d="M3 6l9 7 9-7" fill="none" stroke="#1e1e1e" stroke-width="2"/></svg></span>
      email: info@kranex.org
    </li>
    <li>
      <span class="icon"><svg width="14" height="14" viewBox="0 0 24 24" fill="none" stroke="#1e1e1e" stroke-width="2" aria-hidden="true"><circle cx="12" cy="12" r="9"/><path d="M3 12h18M12 3c3 3 3 15 0 18M12 3c-3 3-3 15 0 18"/></svg></span>
      www.kranex.org
    </li>
  </ul>
</section>

</body>
</html>
```